Business Card Design.

Life and Wellness Coach
www.brightpathwell.com
Want to use my name as the logo it could be the initials TRH or my full name. I want to trade mark me.
I like clean lines and simple designs, but it pops using the colors scheme (one or two colors) on the website.
I provide life and health coaching virtually and in person. My services include: Nutrition Response Testing, Allergy Elimination Testing, Wellness Coaching, Life Coaching. Life and Health Assessments, and I sell foundational health products and specialized nutrition. Use colors that represent healing and trust.
Target Market(s)
Women for the ages of 30 - 60
Industry/Entity Type
Health
Contact Information for Business Card
Tessa Ravenna Holloway
Life and Wellness Coach
tessa@coachtrh.com
www.brightpathwell.com
443-781-6392
Health is not an event it's a lifestyle (tag line or if you have a better tag line)

```html
<!DOCTYPE html>
<html lang="en">
<head>
<meta charset="utf-8">
<title>Tessa Ravenna Holloway – Business Card</title>
<link href="https://fonts.googleapis.com/css2?family=Source+Sans+3:wght@400;700&display=swap" rel="stylesheet">
<style>
  :root {
    --backdrop: #e6e7e9;
    --card: #ffffff;
    --ink: #3a3a3a;
    --gold: #b58a2e;
    --gold-soft: rgba(181, 138, 46, 0);
  }
  html, body {
    margin: 0;
    padding: 0;
    width: 1200px;
    height: 960px;
    overflow: hidden;
    background: var(--backdrop);
    font-family: "Source Sans 3", "Myriad Pro", Arial, sans-serif;
  }
  .business-card {
    position: absolute;
    left: 180px;
    top: 240px;
    width: 840px;
    height: 480px;
    background: var(--card);
    color: var(--ink);
    text-align: center;
  }
  .business-card > * {
    position: absolute;
    left: 0;
    right: 0;
    margin: 0;
  }
  .holder-name {
    top: 38px;
    font-size: 25px;
    line-height: 26px;
    font-weight: 400;
  }
  .holder-title {
    top: 65px;
    font-size: 22px;
    line-height: 22px;
    color: var(--gold);
  }
  .brand-initials {
    top: 185px;
    font-size: 64px;
    line-height: 64px;
    font-weight: 700;
    letter-spacing: 4px;
    color: var(--ink);
  }
  .divider-line {
    top: 251px;
    height: 3px;
    background: linear-gradient(to right, var(--gold-soft), var(--gold) 50%, var(--gold-soft));
  }
  .tagline {
    top: 262px;
    font-size: 22px;
    line-height: 22px;
    color: var(--gold);
  }
  .contact-list {
    top: 389px;
    font-size: 21px;
    line-height: 20px;
    font-style: normal;
  }
  .contact-list span { display: block; }
</style>
</head>
<body>
  <section class="business-card">
    <h1 class="holder-name">Tessa Ravenna Holloway</h1>
    <p class="holder-title">Life and Wellness Coach</p>
    <div class="brand-initials">TRH</div>
    <div class="divider-line"></div>
    <p class="tagline">Health is not an event it's a lifestyle</p>
    <address class="contact-list">
      <span class="contact-phone">443-781-6392</span>
      <span class="contact-web">www.brightpathwell.com</span>
      <span class="contact-email">tessa@coachtrh.com</span>
    </address>
  </section>
</body>
</html>
```